Torvel, Inc. new buisness cards - brand guide included

We need new business cards. SLEAK SIMPLE FINANCE. They must include a place for NAME, TITLE, CELL, OFFICE PHONE, EMAIL. they also must include our services across the bottom. AIR, OCEAN, FTL, LTL, EXPRESS. for reference this will be being handed to some of the most prestigious shipping companies in a america.

Target Market(s)

Finance and corporate

Contact Information for Business Card

We need new business cards. SLEAK SIMPLE FINANCE. They must include a place for NAME, TITLE, CELL, OFFICE PHONE, EMAIL. they also must include our services across the bottom. AIR, OCEAN, FTL, LTL, EXPRESS.

Requirements
Must have
• We need new business cards. SLEAK SIMPLE FINANCE. They must include a place for NAME, TITLE, CELL, OFFICE PHONE, EMAIL. they also must include our services across the bottom. AIR, OCEAN, FTL, LTL, EXPRESS.
Nice to have
• USE THE COLORS AND LOGO IN THE BRAND GUIDE :)

```html
<!DOCTYPE html>
<html lang="en">
<head>
<meta charset="utf-8">
<title>Torvel, Inc. — Business Cards</title>
<link href="https://fonts.googleapis.com/css2?family=Open+Sans:wght@400;600;700&display=swap" rel="stylesheet">
<style>
  :root {
    --page-bg: #e9e9e9;
    --card-bg: #2b2b2b;
    --card-bg-deep: #262626;
    --ink-light: #efece4;
    --ink-muted: #cfccc4;
    --rule: #8d8a84;
    --pill-bg: #f1eee6;
    --pill-ink: #2b2b2b;
  }
  * { margin: 0; padding: 0; box-sizing: border-box; }
  html, body {
    width: 1200px; height: 801px; overflow: hidden;
    background: var(--page-bg);
    font-family: "Open Sans", sans-serif;
  }
  .sheet {
    position: relative; width: 1200px; height: 801px;
    display: flex; align-items: center; justify-content: center; gap: 36px;
  }
  .card {
    position: relative; width: 560px; height: 320px;
    background: var(--card-bg); color: var(--ink-light);
    box-shadow: 0 10px 28px rgba(0,0,0,.22);
    overflow: hidden;
  }

  /* Front */
  .brand {
    position: absolute; top: 48px; right: 48px;
    display: flex; align-items: center; gap: 12px;
    font-weight: 600; font-size: 40px; letter-spacing: 3px;
    color: var(--ink-light);
  }
  .brand-square { width: 14px; height: 14px; background: var(--ink-light); }
  .holder { position: absolute; left: 40px; top: 150px; }
  .holder-name { font-weight: 700; font-size: 22px; letter-spacing: .5px; }
  .holder-title { font-size: 15px; color: var(--ink-muted); margin-top: 1px; }
  .divider {
    position: absolute; left: 40px; right: 40px; top: 212px;
    height: 1px; background: var(--rule);
  }
  .contacts {
    position: absolute; left: 40px; top: 224px;
    list-style: none; font-size: 14.5px; line-height: 20px;
  }
  .contacts li { display: flex; align-items: center; gap: 8px; }
  .contacts svg { width: 13px; height: 13px; flex: none; }
  .icon-fill { fill: var(--ink-light); }
  .icon-line { fill: none; stroke: var(--ink-light); stroke-width: 1.4; }
  .address {
    position: absolute; right: 40px; top: 226px; text-align: right;
    font-size: 14.5px; line-height: 20px; color: var(--ink-muted);
  }

  /* Back */
  .card-back { background: var(--card-bg-deep); }
  .pattern-area {
    position: absolute; inset: 0;
    background: linear-gradient(135deg, #262626 0%, #2e2e2e 50%, #242424 100%);
  }
  .back-content {
    position: absolute; inset: 0;
    display: flex; flex-direction: column; align-items: center; justify-content: center;
  }
  .back-brand {
    display: flex; align-items: center; gap: 14px;
    font-weight: 600; font-size: 48px; letter-spacing: 4px;
  }
  .back-brand .brand-square { width: 16px; height: 16px; }
  .services-label {
    margin-top: 14px; background: var(--pill-bg); color: var(--pill-ink);
    font-weight: 700; font-size: 19px; letter-spacing: .5px;
    padding: 3px 22px; border-radius: 20px;
  }
  .services {
    margin-top: 12px; list-style: none; display: flex; gap: 14px;
    font-size: 24px; letter-spacing: .5px;
  }
  .services li::before {
    content: ""; display: inline-block; width: 8px; height: 8px;
    border-radius: 50%; background: var(--ink-light);
    margin-right: 8px; vertical-align: middle; position: relative; top: -2px;
  }
</style>
</head>
<body>
<main class="sheet">
  <section class="card card-front" aria-label="Business card front">
    <div class="brand"><span class="brand-square"></span>Torvel</div>
    <div class="holder">
      <p class="holder-name">DANIEL REEVES</p>
      <p class="holder-title">Managing Director</p>
    </div>
    <div class="divider"></div>
    <ul class="contacts">
      <li><svg viewBox="0 0 16 16"><path class="icon-fill" d="M3 1h3l1.5 4-2 1.2a9 9 0 0 0 4.3 4.3L11 8.5l4 1.5v3a2 2 0 0 1-2 2A12 12 0 0 1 1 3a2 2 0 0 1 2-2z"/></svg>044-555 018 246</li>
      <li><svg viewBox="0 0 16 16"><path class="icon-fill" d="M4 0h8a1 1 0 0 1 1 1v14a1 1 0 0 1-1 1H4a1 1 0 0 1-1-1V1a1 1 0 0 1 1-1zm1 2v10h6V2z"/></svg>044-555 037 912</li>
      <li><svg viewBox="0 0 16 16"><path class="icon-fill" d="M1 3h14v10H1zm1.5 1.5v.3L8 9l5.5-4.2v-.3z"/></svg>info@torvelinc.com</li>
      <li><svg viewBox="0 0 16 16"><circle class="icon-line" cx="8" cy="8" r="6.8"/><ellipse class="icon-line" cx="8" cy="8" rx="3" ry="6.8"/><path class="icon-line" d="M1.2 8h13.6"/></svg>www.torvelinc.com</li>
    </ul>
    <p class="address">Your Address, City<br>State, Zip 0000</p>
  </section>

  <section class="card card-back" aria-label="Business card back">
    <div class="pattern-area" role="img" aria-label="Tone-on-tone embossed brand pattern covering the card"></div>
    <div class="back-content">
      <div class="back-brand"><span class="brand-square"></span>Torvel</div>
      <p class="services-label">OUR SERVICES</p>
      <ul class="services">
        <li>AIR</li><li>OCEAN</li><li>FTL</li><li>LTL</li><li>EXPRESS</li>
      </ul>
    </div>
  </section>
</main>
</body>
</html>
```